Package Card - Horse Products

I require a card design for the top of a package (see photo). This product is a number holder that gets pinned on to a horse bridle or saddle blanket for competitions. It is a high quality, genuine leather, and premium product.Card is 15cm across and 6cm high. Requirements:Must have - Logo, -"Equestrian Number Holder"- Place on back for barcodeAnything else is up to you! Suggestions and ideas welcome. Card back colour can be any colour.My outcome is for it to look like a premium product

Target Market(s)

High end equestrian competitors

Colors
fbf289

Requirements
Must have
• Logo
• "Equestrian Number Holder"
• "Genuine Leather"
• Room on the back for a barcode sticker
Nice to have
• Should look up market and elegant

```html
<!DOCTYPE html>
<html lang="en">
<head>
<meta charset="utf-8">
<title>Saltmarsh Equestrian – Number Holder Package Card</title>
<link rel="stylesheet" href="https://fonts.googleapis.com/css2?family=Cinzel:wght@400;600&display=swap">
<style>
  :root {
    --page-grey: #d4d4d6;
    --card-white: #ffffff;
    --ink-black: #050607;
    --gold-deep: #c47a2e;
    --gold-mid: #d9a443;
    --gold-light: #f3cd72;
  }
  * { margin: 0; padding: 0; box-sizing: border-box; }
  html, body {
    width: 1200px;
    height: 999px;
    overflow: hidden;
    background: var(--page-grey);
  }
  .package-card {
    position: absolute;
    left: 24px;
    top: 38px;
    width: 1152px;
    height: 922px;
    background: var(--card-white);
    overflow: hidden;
    font-family: "Cinzel", serif;
  }
  .barcode-area {
    position: absolute;
    left: 260px;
    top: 58px;
    width: 632px;
    height: 215px;
    background: var(--ink-black);
  }
  .barcode-label {
    position: absolute;
    left: 0;
    right: 40px;
    top: 78px;
    text-align: center;
    color: var(--card-white);
    font-size: 42px;
    font-weight: 400;
    letter-spacing: 1px;
    transform: rotate(180deg);
  }
  .material-label {
    position: absolute;
    left: 0;
    right: 0;
    top: 304px;
    text-align: center;
    color: var(--ink-black);
    font-size: 52px;
    font-weight: 600;
    letter-spacing: 1px;
    transform: rotate(180deg);
  }
  .pin-hole {
    position: absolute;
    left: 551px;
    width: 50px;
    height: 50px;
    border-radius: 50%;
    background: var(--ink-black);
  }
  .pin-hole--upper { top: 379px; }
  .pin-hole--lower { top: 490px; }
  .brand-name {
    position: absolute;
    left: 0;
    right: 0;
    top: 600px;
    display: flex;
    align-items: center;
    justify-content: center;
    gap: 18px;
    color: var(--ink-black);
    font-size: 34px;
    font-weight: 400;
    letter-spacing: 4px;
    line-height: 1;
  }
  .brand-name__dot {
    width: 14px;
    height: 14px;
    border-radius: 50%;
    background: var(--gold-mid);
  }
  .base-wave {
    position: absolute;
    left: 0;
    top: 0;
    width: 1152px;
    height: 922px;
  }
  .product-title {
    position: absolute;
    left: 0;
    right: 0;
    top: 840px;
    text-align: center;
    color: var(--card-white);
    font-size: 51px;
    font-weight: 400;
    letter-spacing: 1.5px;
  }
</style>
</head>
<body>
  <main class="package-card">
    <div class="barcode-area"><span class="barcode-label">Barcode</span></div>
    <p class="material-label">Genuine Leather</p>
    <span class="pin-hole pin-hole--upper"></span>
    <span class="pin-hole pin-hole--lower"></span>

    <h1 class="brand-name">
      <span class="brand-name__dot"></span>
      <span class="brand-name__text">Saltmarsh Equestrian</span>
    </h1>

    <svg class="base-wave" viewBox="0 0 1152 922" aria-hidden="true">
      <defs>
        <linearGradient id="gold-ribbon" x1="0" y1="0" x2="1" y2="0">
          <stop offset="0" stop-color="var(--gold-mid)"/>
          <stop offset="0.45" stop-color="var(--gold-light)"/>
          <stop offset="0.7" stop-color="var(--gold-deep)"/>
          <stop offset="1" stop-color="var(--gold-deep)"/>
        </linearGradient>
      </defs>
      <path fill="url(#gold-ribbon)"
            d="M0 695 C 330 705, 620 790, 820 812 C 970 822, 1090 755, 1152 718
               L1152 724 C 1080 762, 930 818, 776 824 C 580 832, 280 752, 0 767 Z"/>
      <path fill="var(--ink-black)"
            d="M0 767 C 280 752, 580 832, 776 824 C 930 818, 1080 762, 1152 724
               L1152 922 L0 922 Z"/>
    </svg>

    <p class="product-title">Equestrian Number Holder</p>
  </main>
</body>
</html>
```